Structural Engineering Company needs ad for magazine

We are an engineering office for structural engineering in the entertainment industry. Our focus are concert stages, festival structures, grand stands and exhibition booths. Our customers are mainly from Europe, we realize the projects worldwide. Typical customers are designer, architects, stage builders, exhibition builder and technical service provider. We are creating structural analyses, technical consulting, technical drawings and risk assessment. We are working on mid size and major events.
Some technical notes:
- CMYK profile needed, minimum 300 dpi for raster graphic
- Our primary color is Petrol. Favourite is petrol, coral and grey (black). Please use palette shown below.
- Our font in documents is Myriad. Regular at 10 pt for text and Light at 16-24pt for titles.
- The format for the ad is 61 x 127 mm (portrait) or 185 x 46 mm (landscape). Which one is up to you.
To the content:
- For contact details we just want to provide our web address "belsokar.de" and/or our e-mail "info@belsokar.de"
- Attached are some Logo files and photos.
- The ad do not advertise a specific product. It is more a general advertisement for the company.
- The language for the ad should be German. Below are keywords in English and corresponding German translation. You do not need to place all Keywords, it is just a brainstorming list to help you. You are also welcome to use other text. We will help with translation, if necessary.
- we like discussing ideas to get better results, so also if you have questions, please ask.
- If you need information that we haven't thought of yet, please ask.
Our slogan (also in Germany): event meets engineering
Service Keywords EN / DE
- Structural Analysis / Statische Berechnungen
- Risk Assessment / Risikobewertungen
- Consulting & Design / Beratung & Konstruktion
Technical Keywords EN / DE
- Stage machinery / Bühnentechnik
- Scaffolding / Gerüstbau
- Exhibition Booths / Messebauten
- Tents / Zelte
- Temporary Structures / Fliegende Bauten
- Truss / Traversen
- Stages / Bühnen
- Grand Stands / Tribünen
- Leightweight Construction / Leichtbau
- Steel Construction / Stahlbau
- Amusement Rides / Fahrgeschäfte
Look and feel
Each slider illustrates characteristics of the customer's brand and the style your logo design should communicate.

```html
<!DOCTYPE html>
<html lang="de">
<head>
<meta charset="utf-8">
<title>Event meets Engineering – Belsokar Anzeige</title>
<link rel="stylesheet" href="https://fonts.googleapis.com/css2?family=Source+Sans+3:wght@400;600;700&display=swap">
<style>
  :root {
    --page-bg: #d9d9d9;
    --petrol: #33b8d5;
    --ink-dark: #2a0f1f;
    --footer-black: #000000;
    --text-light: #ffffff;
    --bg-maroon: #1d0b16;
    --bg-plum: #3a1436;
    --bg-violet: #4b2574;
    --bg-glow: #7256c9;
  }
  * { margin: 0; padding: 0; box-sizing: border-box; }
  html, body { width: 1200px; height: 904px; overflow: hidden; }
  body {
    background: var(--page-bg);
    font-family: "Source Sans 3", "Myriad Pro", sans-serif;
    position: relative;
  }
  .ad {
    position: absolute;
    left: 40px; top: 312px;
    width: 1120px; height: 279px;
    overflow: hidden;
    color: var(--text-light);
  }
  .ad-backdrop {
    position: absolute; inset: 0;
    background:
      radial-gradient(ellipse 260px 200px at 1060px 40px, rgba(114,86,201,0.75), transparent 70%),
      radial-gradient(ellipse 240px 220px at 1080px 240px, rgba(94,66,200,0.7), transparent 70%),
      radial-gradient(ellipse 380px 260px at 560px 60px, rgba(90,30,90,0.55), transparent 75%),
      linear-gradient(100deg, var(--bg-maroon) 0%, var(--bg-plum) 40%, var(--bg-violet) 80%, #5a36a8 100%);
  }
  .slogan-band {
    position: absolute; left: 0; top: 16px;
    width: 500px; height: 48px;
    background: var(--petrol);
    clip-path: polygon(0 0, 100% 0, 471px 100%, 0 100%);
  }
  .slogan {
    position: absolute; left: 36px; top: 20px;
    font-size: 36px; line-height: 40px; font-weight: 700;
    letter-spacing: -0.8px;
    color: var(--ink-dark);
    white-space: nowrap;
  }
  .section-title {
    position: absolute;
    font-size: 21px; line-height: 24px; font-weight: 700;
    letter-spacing: -0.3px;
    color: var(--petrol);
    white-space: nowrap;
  }
  .section-title--service { left: 37px; top: 79px; }
  .section-title--technical { left: 515px; top: 49px; }
  .keyword-list {
    position: absolute;
    list-style: none;
  }
  .keyword-list li {
    position: relative;
    height: 30px;
    padding-left: 22px;
    font-size: 18px; line-height: 22px;
    white-space: nowrap;
  }
  .keyword-list .tick {
    position: absolute; left: 0; top: 4px;
    width: 14px; height: 14px;
  }
  .keyword-list--service { left: 38px; top: 109px; }
  .keyword-list--technical-a { left: 515px; top: 79px; }
  .keyword-list--technical-b { left: 867px; top: 79px; }
  .contact-footer {
    position: absolute; left: 0; top: 206px;
    width: 449px; height: 73px;
    background: var(--footer-black);
    clip-path: polygon(0 0, 100% 0, 422px 100%, 0 100%);
  }
  .company-name {
    position: absolute; left: 37px; top: 229px;
    font-size: 24px; line-height: 28px; font-weight: 600;
    letter-spacing: 5px;
    color: var(--text-light);
  }
  .contact-list {
    position: absolute; left: 257px; top: 224px;
    list-style: none;
  }
  .contact-list li {
    position: relative;
    height: 21px;
    padding-left: 15px;
    font-size: 16px; line-height: 20px;
  }
  .contact-list .contact-icon {
    position: absolute; left: 0; top: 4px;
    width: 12px; height: 12px;
  }
  .accent-rule {
    position: absolute; left: 422px; top: 272px;
    width: 698px; height: 7px;
    background: var(--petrol);
  }
</style>
</head>
<body>
  <svg width="0" height="0" style="position:absolute" aria-hidden="true">
    <defs>
      <symbol id="tick" viewBox="0 0 14 14">
        <circle cx="7" cy="7" r="7" fill="#33b8d5"/>
        <path d="M3.8 7.2 L6.1 9.4 L10.3 4.9" fill="none" stroke="#2a0f1f" stroke-width="1.8" stroke-linecap="round" stroke-linejoin="round"/>
      </symbol>
      <symbol id="icon-mail" viewBox="0 0 12 12">
        <circle cx="6" cy="6" r="5.3" fill="none" stroke="#33b8d5" stroke-width="1.4"/>
        <rect x="3.2" y="4" width="5.6" height="4" fill="none" stroke="#33b8d5" stroke-width="1"/>
        <path d="M3.2 4 L6 6.2 L8.8 4" fill="none" stroke="#33b8d5" stroke-width="1"/>
      </symbol>
      <symbol id="icon-web" viewBox="0 0 12 12">
        <circle cx="6" cy="6" r="5.3" fill="none" stroke="#33b8d5" stroke-width="1.4"/>
        <ellipse cx="6" cy="6" rx="2" ry="4.3" fill="none" stroke="#33b8d5" stroke-width="0.9"/>
        <path d="M1.5 6 H10.5 M2.3 3.8 H9.7 M2.3 8.2 H9.7" stroke="#33b8d5" stroke-width="0.9"/>
      </symbol>
    </defs>
  </svg>

  <section class="ad">
    <div class="ad-backdrop" role="img" aria-label="Blurred stage lighting photograph in maroon and violet tones"></div>

    <div class="slogan-band"></div>
    <h1 class="slogan">EVENT MEETS ENGINEERING</h1>

    <h2 class="section-title section-title--service">SERVICE KEYWORDS EN / DE</h2>
    <ul class="keyword-list keyword-list--service">
      <li><svg class="tick"><use href="#tick"/></svg>Structural Analysis / Statische Berechnungen</li>
      <li><svg class="tick"><use href="#tick"/></svg>Risk Assessment / Risikobewertungen</li>
      <li><svg class="tick"><use href="#tick"/></svg>Consulting &amp; Design / Beratung &amp; Konstruktion</li>
    </ul>

    <h2 class="section-title section-title--technical">TECHNICAL KEYWORDS EN / DE</h2>
    <ul class="keyword-list keyword-list--technical-a">
      <li><svg class="tick"><use href="#tick"/></svg>Stage machinery / Bühnentechnik</li>
      <li><svg class="tick"><use href="#tick"/></svg>Exhibition Booths / Messebauten</li>
      <li><svg class="tick"><use href="#tick"/></svg>Leightweight Construction / Leichtbau</li>
      <li><svg class="tick"><use href="#tick"/></svg>Amusement Rides / Fahrgeschäfte</li>
      <li><svg class="tick"><use href="#tick"/></svg>Steel Construction / Stahlbau</li>
      <li><svg class="tick"><use href="#tick"/></svg>Temporary Structures / Fliegende Bauten</li>
    </ul>
    <ul class="keyword-list keyword-list--technical-b">
      <li><svg class="tick"><use href="#tick"/></svg>Grand Stands / Tribünen</li>
      <li><svg class="tick"><use href="#tick"/></svg>Scaffolding / Gerüstbau</li>
      <li><svg class="tick"><use href="#tick"/></svg>Truss / Traversen</li>
      <li><svg class="tick"><use href="#tick"/></svg>Stages / Bühnen</li>
      <li><svg class="tick"><use href="#tick"/></svg>Tents / Zelte</li>
    </ul>

    <div class="contact-footer"></div>
    <p class="company-name">BELSOKAR</p>
    <ul class="contact-list">
      <li><svg class="contact-icon"><use href="#icon-mail"/></svg>info@belsokar.de</li>
      <li><svg class="contact-icon"><use href="#icon-web"/></svg>belsokar.de</li>
    </ul>

    <div class="accent-rule"></div>
  </section>
</body>
</html>
```